Refresh of graphic design for existing website

We would like to refresh our website. Please see the attached design specifications.

Industry/Entity Type

Graphic Design

```html
<!DOCTYPE html>
<html lang="en">
<head>
<meta charset="utf-8">
<title>Apex Tooling Council</title>
<link href="https://fonts.googleapis.com/css2?family=Open+Sans:wght@400;600;700&family=Oswald:wght@400;500&display=swap" rel="stylesheet">
<style>
:root{
  --blue:#2b7ec1;
  --blue-dark:#1f669f;
  --ink:#2f2f2f;
  --muted:#777;
  --band:#eeeeee;
  --footer:#2a2a2a;
  --footer-deep:#1f1f1f;
  --line:#dcdcdc;
  --white:#fff;
}
*{box-sizing:border-box;margin:0;padding:0}
html,body{width:1200px;height:2272px;overflow:hidden}
body{font-family:"Open Sans",Arial,sans-serif;color:var(--ink);background:var(--white);font-size:13px;line-height:1.55}
.wrap{width:1000px;margin:0 auto;position:relative}
a{color:inherit;text-decoration:none}
.h-sec{font-family:"Oswald",Arial,sans-serif;font-weight:500;font-size:22px;letter-spacing:.5px;text-transform:uppercase;color:var(--ink)}
.h-sec span{color:var(--blue)}
.btn{display:inline-block;background:var(--blue);color:var(--white);font-size:12px;padding:8px 18px;border-radius:2px}
.more{color:var(--blue);font-size:12px;font-weight:600}

/* header */
.site-header{height:135px}
.brand{position:absolute;left:0;top:36px;display:flex;align-items:center;gap:10px}
.brand-dot{width:22px;height:22px;border-radius:50%;background:var(--blue)}
.brand-name{font-size:40px;font-weight:700;color:var(--blue);line-height:1}
.util{position:absolute;right:0;top:30px;display:flex;gap:8px}
.util input{width:110px;height:26px;border:1px solid var(--line);font:12px "Open Sans",sans-serif;padding:0 8px;color:var(--muted)}
.util .login{height:26px;background:var(--blue);color:#fff;font-size:12px;padding:4px 16px}
.nav{position:absolute;right:0;top:82px;display:flex;gap:6px;font-size:13px;font-weight:600}
.nav a{padding:8px 12px;color:#444}
.nav a.active{border:1px solid var(--blue);color:var(--blue);border-radius:2px}

/* hero */
.hero{height:520px;position:relative;background:linear-gradient(135deg,#6a6f73 0%,#3b3f44 45%,#8a8d8f 70%,#2d3033 100%)}
.hero-cap{position:absolute;left:505px;top:440px;font-family:"Oswald",sans-serif;font-size:26px;color:#fff;line-height:1.2;text-transform:uppercase}

/* welcome */
.welcome{height:285px;text-align:center;padding-top:32px}
.welcome .h-sec{font-size:30px}
.welcome p{width:820px;margin:18px auto 24px;color:var(--muted);font-size:13px}

/* band */
.band{height:640px;background:var(--band);padding-top:85px}
.cols{display:flex;justify-content:space-between}
.col-l{width:520px}.col-r{width:440px}
.video{margin-top:22px;height:290px;background:linear-gradient(160deg,#9fa4a8,#5f656b 60%,#c9c9c9);position:relative}
.play{position:absolute;left:230px;top:115px}
.item-title{font-weight:700;font-size:13px;text-transform:uppercase;margin-top:18px}
.col-l p{color:var(--muted);font-size:12px;margin:8px 0 14px}
.event{display:flex;gap:18px;margin-top:22px}
.event:first-of-type{margin-top:26px}
.thumb{width:110px;height:120px;flex:none;background:linear-gradient(150deg,#b7b2aa,#6f6a63)}
.event h4{font-size:13px;text-transform:uppercase;margin-top:4px}
.date{font-size:11px;color:var(--muted);margin:4px 0}
.event p{font-size:12px;color:var(--muted)}

/* news / blog */
.news{height:460px;padding-top:50px}
.post{margin-top:24px}
.post h4{font-size:12px;text-transform:uppercase}
.post p{font-size:12px;color:var(--muted);margin:4px 0}
.blog{display:flex;gap:18px;margin-top:24px}
.blog .thumb{height:110px}
.blog h4{font-size:12px;text-transform:uppercase}
.blog p{font-size:12px;color:var(--muted);margin:4px 0}

/* footer */
.site-footer{height:212px;background:var(--footer);color:#cfcfcf;padding-top:32px}
.f-brand .brand-name{font-size:30px;color:#fff}
.f-brand p{width:200px;font-size:11px;margin-top:10px;color:#aaa}
.f-col h5{font-family:"Oswald",sans-serif;font-weight:400;font-size:17px;color:#fff;text-transform:uppercase;margin-bottom:12px}
.links{display:grid;grid-template-columns:170px 170px;font-size:11px;row-gap:4px}
.links a::before{content:"› ";color:var(--blue)}
.contact div{display:flex;gap:8px;font-size:11px;margin-bottom:8px}
.bar{height:28px;background:var(--footer-deep);color:#999;font-size:10px}
.bar .wrap{display:flex;justify-content:space-between;align-items:center;height:28px}
.social{display:flex;gap:6px}
.social i{width:16px;height:16px;border-radius:50%;border:1px solid #777;display:block}
</style>
</head>
<body>

<header class="site-header">
  <div class="wrap">
    <a class="brand" href="#"><span class="brand-dot"></span><span class="brand-name">ATC</span></a>
    <div class="util">
      <input type="text" value="Email address...">
      <input type="password" value="Password...">
      <a class="login" href="#">Login</a>
    </div>
    <nav class="nav">
      <a class="active" href="#">Home</a><a href="#">About ATC</a><a href="#">News</a><a href="#">Membership</a><a href="#">Events</a><a href="#">Members Only</a><a href="#">Industry Outreach</a>
    </nav>
  </div>
</header>

<section class="hero" role="img" aria-label="Photo of industry members inspecting an open car engine bay">
  <div class="hero-cap">Segments of the equipment<br>and tool industry</div>
</section>

<section class="welcome">
  <h2 class="h-sec">Welcome to <span>Apex Tooling Council</span></h2>
  <p>The Apex Tooling Council brings together makers of service equipment, diagnostic tools and information so the whole repair trade can work from shared data. For decades our members have met to solve common problems, share early access to vehicle details and help shops fix today's cars right the first time, every time, in every bay.</p>
  <a class="btn" href="#">Read more info</a>
</section>

<section class="band">
  <div class="wrap cols">
    <div class="col-l">
      <h3 class="h-sec">Latest <span>Videos</span></h3>
      <div class="video" role="img" aria-label="Video still of a vehicle on a workshop lift">
        <svg class="play" width="60" height="60" viewBox="0 0 60 60"><circle cx="30" cy="30" r="29" fill="rgba(0,0,0,.55)"/><path d="M24 18 L42 30 L24 42 Z" fill="#fff"/></svg>
      </div>
      <div class="item-title">Across accumulation showroom</div>
      <p>Members walk through the new service lane layout and show how shared scan data helps a technician find the fault on the first visit, then talk about what the next model years will bring.</p>
      <a class="btn" href="#">View more info</a>
    </div>
    <div class="col-r">
      <h3 class="h-sec">Upcoming <span>Events</span></h3>
      <div class="event">
        <div class="thumb" role="img" aria-label="Photo of a trade show hall"></div>
        <div><h4>Parts Expo</h4><div class="date">03 Nov 2015</div><p>Parts Expo is a big gathering for the aftermarket trade, with buyers and makers.</p><a class="more" href="#">Read More »</a></div>
      </div>
      <div class="event">
        <div class="thumb" role="img" aria-label="Photo of a show floor with display vehicles"></div>
        <div><h4>Motor Trade Show</h4><div class="date">03 Nov 2015</div><p>The Motor Trade Show is a leading event for specialty auto parts and tools.</p><a class="more" href="#">Read More »</a></div>
      </div>
      <div class="event">
        <div class="thumb" role="img" aria-label="Photo of attendees at a technical meeting"></div>
        <div><h4>Winter Tech Days</h4><div class="date">20 Jan 2015</div><p>Winter Tech Days is the one true and equipment meeting.</p><a class="more" href="#">Read More »</a></div>
      </div>
    </div>
  </div>
</section>

<section class="news">
  <div class="wrap cols">
    <div class="col-l">
      <h3 class="h-sec">Industry <span>News</span></h3>
      <div class="post">
        <h4>Automakers commit to making automatic braking standard</h4>
        <div class="date">17 Sep 2015</div>
        <p>Most carmakers have agreed to fit automatic braking across their lineups, a step that will shape how shops calibrate and test.</p>
        <a class="more" href="#">Read More »</a>
      </div>
      <div class="post">
        <h4>How shops impact car-buying decisions</h4>
        <div class="date">08 Sep 2015</div>
        <p>A new survey finds trusted repair shops play a growing role in what drivers choose to buy next.</p>
        <a class="more" href="#">Read More »</a>
      </div>
    </div>
    <div class="col-r">
      <h3 class="h-sec">Latest <span>Blog</span></h3>
      <div class="blog">
        <div class="thumb" role="img" aria-label="Photo of council members at a meeting table"></div>
        <div><h4>Apex Tooling Council</h4><div class="date">10 Aug 2015</div><p>Council names new officers and board members to steer its next term.</p><a class="more" href="#">Read More »</a></div>
      </div>
      <div class="blog">
        <div class="thumb" role="img" aria-label="Photo of a show floor"></div>
        <div><h4>Motor Trade Show</h4><div class="date">03 Nov 2015</div><p>The show is a prime venue for the equipment and tool trade.</p><a class="more" href="#">Read More »</a></div>
      </div>
    </div>
  </div>
</section>

<footer>
  <div class="site-footer">
    <div class="wrap cols">
      <div class="f-brand">
        <span class="brand-name">ATC</span>
        <p>A trade council that brings tool and equipment makers together to share vehicle data and support the repair trade.</p>
      </div>
      <div class="f-col">
        <h5>Quick Links</h5>
        <div class="links">
          <a href="#">ATC Tech Library</a><a href="#">Member Research Groups</a>
          <a href="#">ATC News Blog</a><a href="#">Payment Center</a>
          <a href="#">Member Committees</a><a href="#">Training Program Update</a>
          <a href="#">Industry Participants</a><a href="#">Job Board</a>
          <a href="#">Investment Planning Guide</a><a href="#">Data Log</a>
        </div>
      </div>
      <div class="f-col contact" style="width:200px">
        <h5>Contact Details</h5>
        <div><svg width="12" height="14" viewBox="0 0 12 14"><path d="M6 0a5 5 0 0 0-5 5c0 4 5 9 5 9s5-5 5-9a5 5 0 0 0-5-5z" fill="#2b7ec1"/><circle cx="6" cy="5" r="2" fill="#2a2a2a"/></svg><span>Apex Tooling Council<br>1200 Harbor Lane, Suite 40<br>Millbrook, ST 00000</span></div>
        <div><svg width="12" height="12" viewBox="0 0 12 12"><path d="M2 1h3l1 3-2 1a7 7 0 0 0 3 3l1-2 3 1v3c-6 1-10-4-9-9z" fill="#2b7ec1"/></svg><span>555-014-2276</span></div>
        <div><svg width="12" height="10" viewBox="0 0 12 10"><rect x=".5" y=".5" width="11" height="9" fill="none" stroke="#2b7ec1"/><path d="M.5 .5 6 5l5.5-4.5" fill="none" stroke="#2b7ec1"/></svg><span>hello@apextooling.example</span></div>
      </div>
    </div>
  </div>
  <div class="bar">
    <div class="wrap"><span>Copyright 2015 Apex Tooling Council. All Rights Reserved.</span><div class="social"><i></i><i></i><i></i></div></div>
  </div>
</footer>

</body>
</html>
```